Web Developer Needs a Business Card Design

I need a personal business card design that represents me as a web developer for potential employers. I would like the background to be a dark color on the front for contrast with my logo and name. The back will have all my information along with a smaller version of the logo. I want something with a modern look and feel, not too conservative. This will be used for potential employers and freelance work.

Industry/Entity Type

Business

Contact Information for Business Card

Front should have my logo and name. The back should have all my personal information which would include: name: Tom Varnuch, phone: 570-614-9083, email: tomvarnuch@mailnest.example, website url: www.tomvarnuch.example, logo, web developer.

Font styles to use
Sans Serif

Requirements
Must have
• Must include my logo. The color palette base color will be the logo color.

```html
<!DOCTYPE html>
<html lang="en">
<head>
<meta charset="utf-8">
<title>Tom Varnuch — Business Card</title>
<link rel="stylesheet" href="https://fonts.googleapis.com/css2?family=Open+Sans:wght@400;600;700&display=swap">
<style>
  :root {
    --stage: #141414;
    --card: #0b0b0b;
    --card-edge: #1f1f1f;
    --accent: #7fd3c0;
    --ink: #e9e9e9;
  }
  * { margin: 0; padding: 0; box-sizing: border-box; }
  html, body { width: 1200px; height: 864px; overflow: hidden; }
  body {
    background: var(--stage);
    font-family: "Open Sans", Arial, sans-serif;
    position: relative;
  }
  .card {
    position: absolute;
    width: 500px;
    height: 286px;
    background: var(--card);
    border: 1px solid var(--card-edge);
    border-radius: 4px;
  }
  .card--front { left: 630px; top: 170px; }
  .card--back { left: 100px; top: 410px; }

  /* front */
  .front-brand {
    position: absolute;
    inset: 0;
    display: flex;
    flex-direction: column;
    align-items: center;
    justify-content: center;
    gap: 14px;
  }
  .brand-mark {
    display: flex;
    align-items: center;
    gap: 10px;
    color: var(--accent);
    font-weight: 600;
    font-size: 15px;
  }
  .brand-ring {
    width: 46px; height: 46px;
    border: 4px solid var(--accent);
    border-radius: 50%;
  }
  .front-name {
    color: var(--ink);
    font-size: 24px;
    letter-spacing: 1px;
    font-weight: 400;
    text-transform: uppercase;
  }

  /* back */
  .back-brand {
    position: absolute;
    left: 40px; top: 88px;
    width: 150px;
    display: flex;
    flex-direction: column;
    align-items: center;
    gap: 10px;
    color: var(--accent);
    font-weight: 600;
    font-size: 15px;
  }
  .back-brand .brand-ring { width: 80px; height: 80px; border-width: 6px; }
  .divider {
    position: absolute;
    left: 215px; top: 80px;
    width: 1px; height: 126px;
    background: var(--accent);
  }
  .contact {
    position: absolute;
    left: 232px; top: 80px;
    color: var(--ink);
    font-size: 13px;
  }
  .contact-name { color: var(--accent); font-weight: 700; font-size: 15px; }
  .contact-role { margin-bottom: 12px; }
  .contact-row { display: flex; align-items: center; gap: 8px; line-height: 20px; }
  .contact-icon { width: 13px; height: 13px; flex: none; }
</style>
</head>
<body>
  <section class="card card--front" aria-label="Card front">
    <div class="front-brand">
      <div class="brand-mark"><span class="brand-ring"></span>Tom Varnuch</div>
      <h1 class="front-name">Tom Varnuch</h1>
    </div>
  </section>

  <section class="card card--back" aria-label="Card back">
    <div class="back-brand"><span class="brand-ring"></span>Tom Varnuch</div>
    <div class="divider"></div>
    <div class="contact">
      <p class="contact-name">Tom Varnuch</p>
      <p class="contact-role">Web Developer</p>
      <p class="contact-row">
        <svg class="contact-icon" viewBox="0 0 13 13"><rect width="13" height="13" rx="2" fill="var(--accent)"/><path d="M4 3l1.5 0 .7 1.8-1 .7a5 5 0 0 0 2.3 2.3l.7-1 1.8.7V9.5c0 .5-.5.8-1 .7A6.5 6.5 0 0 1 3.3 4c-.1-.5.2-1 .7-1z" fill="var(--card)"/></svg>
        570-614-9083
      </p>
      <p class="contact-row">
        <svg class="contact-icon" viewBox="0 0 13 13"><rect width="13" height="13" rx="2" fill="var(--accent)"/><rect x="3" y="4" width="7" height="5" fill="none" stroke="var(--card)" stroke-width="1"/><path d="M3 4l3.5 3L10 4" fill="none" stroke="var(--card)" stroke-width="1"/></svg>
        tomvarnuch@mailnest.example
      </p>
      <p class="contact-row">
        <svg class="contact-icon" viewBox="0 0 13 13"><rect width="13" height="13" rx="2" fill="var(--accent)"/><circle cx="6.5" cy="6.5" r="3.5" fill="none" stroke="var(--card)" stroke-width="1"/><path d="M3 6.5h7M6.5 3c-1.5 2-1.5 5 0 7M6.5 3c1.5 2 1.5 5 0 7" fill="none" stroke="var(--card)" stroke-width=".8"/></svg>
        www.tomvarnuch.example
      </p>
    </div>
  </section>
</body>
</html>
```